Varemo - Nutritious Snacks and Desserts

We need a creative e-commerce website in which all features--buttons, background, etc.--convey our message: We sell delicious, nutritious snacks and desserts that most closely comply with the paleo diet guidelines. Our first product is Brantoza®--raw, vegan, paleo chocolate balls that are made of dates, coconut, and cocoa. Our products are organic, raw, irresistible and nutritious. We have several versions of Brantoza® in development, as well as mousse, ice cream, and crackers. Our mission is to purvey basic healthy foods. Our motto is, "Fuel for the Daring Trail-Seeker(tm)."

Target Market(s)

Health-conscious professionals who tend to shop at health food stores. Our products also meet the requirements of a gluten-free diet; and they also don't contain refined sugar, so shoppers with gluten and possibly sugar issues are incidental customers.

Industry/Entity Type

Health Product

Coding

Coded - Design and coding required

Number of Pages Required

5+ page

Colors

Designer to choose colors to be used in the design.

Requirements
Must have
• We need at least a home page, a products page, an about-us page, a contact page, and a shopping cart page. We would like to be able to add products on our own later. We should be able to handle some basic coding, especially if it's just a matter of copying and modifying product pages. We would also like the ability in the future to add blogging pages, allowing us to write articles about health food and healthy lifestyle, thus attracting web-traffic (SEO).
• Other features we would like to have:
• Product photo slider on the hopepage
• Back-to-top button at the bottom of the home page
• Make sure the site is mobile-compatible
• A search bar at the top of the homepage
• "Create an account" and "Previous orders"--allowing customers to see their previous orders and reorder what they purchased in the past.
Nice to have
• We would like to convey the paleo theme without actually stating it anywhere. We'll add text as necessary, according to the page layout; you can use ipsum lorem for purpose of demonstration.

```html
<!DOCTYPE html>
<html lang="en">
<head>
<meta charset="utf-8">
<title>Varemo Foods</title>
<link rel="stylesheet" href="https://fonts.googleapis.com/css2?family=Open+Sans:wght@400;600;700;800&display=swap">
<style>
:root{
  --cream:#f1ebe3;
  --tan:#c8a47c;
  --tan-dark:#a8835c;
  --rust:#b5692a;
  --ink:#1e1b17;
  --muted:#8a847c;
  --leaf:#6e9a2c;
  --rule:#2d2a26;
  --button:#3a3328;
  --base:#cdc9ac;
  --white:#ffffff;
}
*{margin:0;padding:0;box-sizing:border-box}
html,body{width:758px;height:1200px;overflow:hidden}
body{position:relative;background:var(--cream);font-family:"Open Sans",Arial,sans-serif;color:var(--ink)}
.abs{position:absolute}

.site-header{position:absolute;left:0;top:0;width:758px;height:53px;background:var(--cream);border-bottom:2px solid var(--rule);z-index:3}
.brand-box{position:absolute;left:42px;top:0;width:93px;height:66px;background:var(--white);border-bottom:4px solid var(--leaf);z-index:4;display:flex;flex-direction:column;align-items:center;justify-content:center;gap:4px}
.brand-dot{width:22px;height:22px;border-radius:50%;background:var(--leaf)}
.brand-name{font-size:15px;font-weight:600;color:var(--leaf);letter-spacing:1px;line-height:1}
.main-nav a{position:absolute;top:22px;font-size:7.5px;font-weight:700;letter-spacing:.9px;color:var(--ink);text-decoration:none}
.main-nav a.active{color:var(--leaf)}
.header-tools svg{position:absolute;top:20px}
.social-dot{position:absolute;top:21px;width:9px;height:9px;border-radius:50%;background:var(--ink)}
.cart-count{position:absolute;left:608px;top:11px;width:8px;height:8px;border-radius:50%;background:var(--leaf);color:#fff;font-size:5px;text-align:center;line-height:8px}

.hero{position:absolute;left:0;top:53px}
.hero-title{position:absolute;left:144px;top:128px;font-size:38px;font-weight:700;color:var(--white);line-height:1}
.hero-tagline{position:absolute;left:150px;top:186px;font-size:19px;font-weight:700;line-height:27px;color:var(--ink)}
.hero-product{position:absolute;left:436px;top:148px;width:220px;height:170px;border-radius:14px 14px 70px 70px;background:linear-gradient(180deg,#fbfaf7 0%,#d8c3a2 35%,#b58f62 70%,#8e6a44 100%)}

.section-title{position:absolute;left:0;width:758px;text-align:center;font-size:27px;font-weight:800;color:var(--rust)}
.intro{position:absolute;left:139px;top:456px;width:480px;text-align:center;font-size:8.3px;line-height:17px}

.product-card{position:absolute;top:610px;width:152px;height:200px;border:1px solid rgba(0,0,0,.05)}
.product-photo{width:152px;height:152px;background:linear-gradient(180deg,#3a3b40 0%,#cfc3ae 35%,#b68e5f 65%,#8f8a86 100%)}
.product-name{margin-top:12px;text-align:center;font-size:11.5px;font-weight:600;color:var(--muted)}
.product-price{text-align:center;font-size:7.5px;color:#aaa39a;margin-top:1px}

.footer-band{position:absolute;left:0;top:868px}
.footer-brand{position:absolute;left:42px;top:975px;display:flex;align-items:center;gap:8px}
.footer-brand .brand-dot{width:34px;height:34px}
.footer-brand .brand-name{font-size:24px}
.footer-heading{position:absolute;font-size:11.5px;font-weight:600}
.follow-box{position:absolute;top:1098px;width:17px;height:17px;border:1px solid var(--ink)}
.follow-box span{position:absolute;left:5px;top:5px;width:5px;height:5px;background:var(--ink)}
.contact-line{position:absolute;left:212px;font-size:8.3px;display:flex;align-items:center;gap:6px}
.contact-line svg{width:8px;height:8px}
.field-label{position:absolute;left:383px;top:1000px;font-size:5.5px;font-weight:700}
.email-field{position:absolute;left:383px;top:1018px;width:154px;height:27px;border:1px solid var(--ink);font-size:6px;color:#bbb;padding:9px 6px}
.signup{position:absolute;left:383px;top:1063px;width:88px;height:25px;background:var(--button);color:#fff;font-size:6.5px;font-weight:700;letter-spacing:2px;text-align:center;line-height:25px}
.quick-link{position:absolute;left:554px;font-size:8.3px}
.base-bar{position:absolute;left:0;top:1160px;width:758px;height:40px;background:var(--base);text-align:center;font-size:5.5px;font-weight:700;line-height:40px}
</style>
</head>
<body>

<header class="site-header">
  <nav class="main-nav">
    <a class="active" style="left:270px">HOME</a>
    <a style="left:311px">ABOUT US</a>
    <a style="left:369px">CONTACT US</a>
    <a style="left:436px">PRODUCTS</a>
  </nav>
  <div class="header-tools">
    <svg style="left:579px" width="11" height="11" viewBox="0 0 11 11"><circle cx="4.5" cy="4.5" r="3.5" fill="none" stroke="#1e1b17" stroke-width="1.3"/><line x1="7" y1="7" x2="10" y2="10" stroke="#1e1b17" stroke-width="1.3"/></svg>
    <svg style="left:598px" width="11" height="12" viewBox="0 0 11 12"><rect x="1" y="4" width="9" height="7.5" fill="none" stroke="#1e1b17" stroke-width="1.2"/><path d="M3.5 4V2.5a2 2 0 0 1 4 0V4" fill="none" stroke="#1e1b17" stroke-width="1.2"/></svg>
    <div class="cart-count">0</div>
    <span class="social-dot" style="left:618px"></span>
    <span class="social-dot" style="left:638px"></span>
    <span class="social-dot" style="left:657px"></span>
    <span class="social-dot" style="left:676px"></span>
    <span class="social-dot" style="left:695px"></span>
  </div>
</header>
<div class="brand-box"><span class="brand-dot"></span><span class="brand-name">varemo</span></div>

<section class="hero">
  <svg width="758" height="275" viewBox="0 0 758 275" role="img" aria-label="Earthy textured stone background">
    <rect width="758" height="275" fill="var(--tan)"/>
    <path d="M0 275 Q379 163 758 275 Z" fill="var(--cream)"/>
  </svg>
</section>
<h1 class="hero-title">Brantoza</h1>
<p class="hero-tagline">Fuel for the daring<br>trail-seeker -100% Natural</p>
<div class="hero-product" role="img" aria-label="Photo of a Brantoza dessert cup"></div>

<h2 class="section-title" style="top:392px">Welcome to Varemo Foods.</h2>
<p class="intro">Our products are raw, organic, vegan, gluten-free, dairy-free, fiber-rich, nutrient-dense, antioxidant-rich real foods with no preservatives, noadded sugar, and no artificial or plant-basedsweeteners. And they are irresistibly scrumptious!</p>

<h2 class="section-title" style="top:528px">Varemo Products.</h2>

<article class="product-card" style="left:42px"><div class="product-photo" role="img" aria-label="Product photo of a dessert cup"></div><div class="product-name">Coming Soon</div><div class="product-price">£120.00</div></article>
<article class="product-card" style="left:213px"><div class="product-photo" role="img" aria-label="Product photo of a dessert cup"></div><div class="product-name">Coming Soon</div><div class="product-price">£120.00</div></article>
<article class="product-card" style="left:384px"><div class="product-photo" role="img" aria-label="Product photo of a dessert cup"></div><div class="product-name">Coming Soon</div><div class="product-price">£120.00</div></article>
<article class="product-card" style="left:554px"><div class="product-photo" role="img" aria-label="Product photo of a Brantoza cup"></div><div class="product-name">Brantoza®</div><div class="product-price">£120.00</div></article>

<footer>
  <svg class="footer-band" width="758" height="76" viewBox="0 0 758 76" role="img" aria-label="Earthy textured stone band">
    <rect width="758" height="76" fill="var(--tan)"/>
    <path d="M0 76 Q379 -44 758 76 Z" fill="var(--cream)"/>
  </svg>

  <div class="footer-brand"><span class="brand-dot"></span><span class="brand-name">varemo</span></div>
  <h3 class="footer-heading" style="left:42px;top:1073px">Follow Us</h3>
  <span class="follow-box" style="left:42px"><span></span></span>
  <span class="follow-box" style="left:65px"><span></span></span>
  <span class="follow-box" style="left:87px"><span></span></span>
  <span class="follow-box" style="left:110px"><span></span></span>
  <span class="follow-box" style="left:133px"><span></span></span>

  <h3 class="footer-heading" style="left:212px;top:965px">Contact Us</h3>
  <div class="contact-line" style="top:992px"><svg viewBox="0 0 8 8"><path d="M0 4 4 0.5 8 4H7V8H1V4Z" fill="#1e1b17"/></svg>41 Fernhollow Road</div>
  <div class="contact-line" style="top:1009px">Alder Springs OR 97021</div>
  <div class="contact-line" style="top:1032px"><svg viewBox="0 0 8 8"><path d="M1 0.5 3 0.5 3.5 2.5 2.3 3.4Q3.3 5 4.6 5.7L5.5 4.5 7.5 5V7Q3.5 7.5 0.5 1.5Z" fill="#1e1b17"/></svg>+100 555 0142</div>
  <div class="contact-line" style="top:1054px"><svg viewBox="0 0 8 8"><rect x="2" y="0.5" width="4" height="7" rx="0.8" fill="none" stroke="#1e1b17"/></svg>+100 555 0142</div>
  <div class="contact-line" style="top:1077px"><svg viewBox="0 0 8 8"><rect x="0.5" y="3" width="7" height="4.5" fill="#1e1b17"/><rect x="2" y="0.5" width="4" height="3" fill="none" stroke="#1e1b17"/></svg>+100 555 0142</div>
  <div class="contact-line" style="top:1100px"><svg viewBox="0 0 8 8"><rect x="0.5" y="1.5" width="7" height="5" fill="#1e1b17"/><path d="M0.5 1.5 4 4.5 7.5 1.5" stroke="#f1ebe3" fill="none" stroke-width=".8"/></svg>hello@varemo.test</div>

  <h3 class="footer-heading" style="left:383px;top:965px">Newsletter Signup</h3>
  <div class="field-label">EMAIL ADDRESS:</div>
  <div class="email-field">Your email address</div>
  <div class="signup">SIGN UP</div>

  <h3 class="footer-heading" style="left:554px;top:965px">Quick Links</h3>
  <div class="quick-link" style="top:992px">Home</div>
  <div class="quick-link" style="top:1015px">About Us</div>
  <div class="quick-link" style="top:1037px">Products</div>
  <div class="quick-link" style="top:1060px">Contact Us</div>

  <div class="base-bar">COPYRIGHT 2015 - ALL RIGHTS RESERVED.</div>
</footer>

</body>
</html>
```